Velquor Web Site

We need a new web site for a new company, Velquor Pty Ltd.
The company will provide services around the Brintara Skyhold and Tallowbench Suite products.
The company theme is "Work is what you do, not where you go." We aim to separate the concepts of data and place. Our clients can access their data anywhere, any time.
The design should look modern, international and should include the Brintara Associate logo.
Updates
My existing web site is visible at http://quennelworks.example. I am hoping that a good designer can provide a fresh look for the business.
Three images for "Cloud" uploaded today.
Target Market(s)
Business of all kinds
Industry/Entity Type
It Company
Requirements
Nice to have
- Colors and themes might reflect Brintara look and style.

```html
<!DOCTYPE html>
<html lang="en">
<head>
<meta charset="utf-8">
<title>Velquor</title>
<link rel="stylesheet" href="https://fonts.googleapis.com/css2?family=Roboto:wght@400;500;700&family=Roboto+Condensed:wght@700&display=swap">
<style>
:root{
  --navy:#2b5585;
  --link:#2e5f99;
  --text:#333;
  --muted:#8a8a8a;
  --line:#d8d8d8;
  --panel:#f3f3f3;
  --white:#fff;
  --sky-light:#7fcdf3;
  --sky-dark:#1f78c0;
  --suite-a:#f7c21c;
  --suite-b:#e8561c;
  --lock:#f3c21b;
}
*{margin:0;padding:0;box-sizing:border-box}
html,body{width:1090px;height:1200px;overflow:hidden}
body{font-family:"Roboto",Arial,sans-serif;color:var(--text);background:var(--white);position:relative}
.wrap{position:absolute;left:146px;width:797px}
.topline{position:absolute;top:0;left:0;width:1090px;height:4px;background:var(--navy)}
.header{position:absolute;top:0;left:0;width:1090px;height:118px;background:linear-gradient(#fff,#f2f2f2)}
.contact-tab{position:absolute;top:4px;right:147px;height:27px;padding:0 12px;background:var(--navy);color:#fff;font-size:11px;font-weight:500;line-height:24px;border-radius:0 0 4px 4px}
.contact-tab .sep{color:#6f93bd;margin:0 8px}
.brand{position:absolute;top:30px;left:148px;display:flex;align-items:center;gap:12px}
.brand-mark{width:88px;height:58px;background:var(--navy);border-radius:6px}
.brand-name{font-family:"Roboto Condensed",Arial,sans-serif;font-weight:700;font-size:38px;color:var(--navy)}
.nav{position:absolute;top:61px;right:147px;display:flex;gap:29px;font-size:11px;color:#222}
.hero{position:absolute;top:118px;left:0;width:1090px;height:376px;
  background:
    radial-gradient(ellipse 320px 220px at 520px 230px,rgba(232,180,150,.85),rgba(232,180,150,0) 70%),
    linear-gradient(105deg,#f4f1ee 0%,#efe3d8 22%,#d9b49b 34%,#3f6d84 46%,#2c7fae 58%,#2a8fc6 66%,#6e3f82 74%,#d24f2a 84%,#c8373a 100%)}
.hero-title{position:absolute;left:146px;top:138px;background:var(--navy);color:#fff;font-size:20px;padding:6px 20px;height:35px}
.hero-sub{position:absolute;left:146px;top:179px;background:var(--navy);color:#fff;font-size:13px;padding:0 21px;height:33px;line-height:33px}
.hero-arrows{position:absolute;left:146px;top:222px;display:flex;gap:5px}
.hero-arrows span{width:30px;height:30px;display:flex;align-items:center;justify-content:center}
.hero-arrows .prev{background:#888}
.hero-arrows .next{background:#333}
.features{position:absolute;top:494px;left:0;width:1090px;height:155px;background:linear-gradient(#fff,#eee);border-bottom:1px solid var(--line)}
.feature{position:absolute;top:0;height:154px;border-left:1px solid var(--line);text-align:center}
.feature h3{font-weight:400;font-size:16px;color:#222;margin-top:22px}
.feature .icon{margin:16px auto 0}
.icon-cloud{width:104px;height:66px;border-radius:33px;background:linear-gradient(160deg,var(--sky-light),var(--sky-dark))}
.icon-suite{width:64px;height:68px;border-radius:4px;background:linear-gradient(135deg,var(--suite-a),var(--suite-b))}
.icon-lock{width:56px;height:56px;margin-top:22px!important;background:var(--lock);transform:rotate(45deg);border:3px solid #222;border-radius:9px}
.section-title{font-size:21px;font-weight:400;color:var(--navy)}
.about{top:668px}
.about p{font-size:10.5px;line-height:12.8px;width:250px;color:#333;margin-top:11px}
.about .first{margin-top:20px}
.read-more{position:absolute;top:159px;left:0;font-size:11px;font-weight:700;color:#111}
.partner-badge{position:absolute;left:268px;top:39px;width:220px;height:127px;border:1px solid var(--line);display:flex;align-items:center;justify-content:center;background:#fff}
.partner-badge div{width:190px;height:100px;border-radius:4px;background:linear-gradient(135deg,#e9f4fb,#e8f5ea)}
.vline{position:absolute;left:667px;top:668px;width:1px;height:183px;border-left:1px dashed var(--line)}
.testimonial{position:absolute;left:703px;top:668px;width:240px}
.testimonial blockquote{font-size:10.5px;line-height:12.7px;margin-top:25px;text-indent:30px;position:relative}
.quote-mark{position:absolute;font-family:Georgia,serif;font-size:34px;color:#b9c6d6;line-height:1}
.testimonial .who{margin-top:26px;font-size:11px;font-weight:500;color:#444}
.testimonial .org{font-size:11px;color:var(--muted)}
.more{position:absolute;right:0;top:166px;font-size:11px;font-weight:700;color:#111}
.divider{position:absolute;left:146px;top:878px;width:797px;border-top:1px dashed var(--line)}
.clients{top:898px}
.view-all{position:absolute;right:0;top:10px;font-size:11px;font-weight:700;color:#111}
.client-row{position:absolute;top:46px;left:0;display:flex;gap:17px}
.client{width:100px;height:58px;border:1px solid var(--line);display:flex;align-items:center;justify-content:center;font-size:10.5px;font-weight:700;color:var(--navy);text-align:center}
.client.dark{background:#7d7f82;color:#fff}
.client.blue{background:#1d8fd6;color:#fff}
.footer{position:absolute;top:1043px;left:0;width:1090px;height:129px;background:var(--panel)}
.fcol{position:absolute;top:20px;font-size:11px;color:var(--link)}
.fcol h4{font-size:11px;font-weight:700;color:var(--navy)}
.fsep{position:absolute;top:20px;height:87px;border-left:1px dashed #ccc}
.quick a{display:block;line-height:16px;color:var(--link);text-decoration:none}
.phone{font-size:16px;margin-top:3px}
.email{text-decoration:underline}
.social{display:flex;gap:10px;margin-top:10px}
.social span{display:flex;align-items:center;gap:3px;font-size:10px;color:var(--navy)}
.social i{width:12px;height:12px;border-radius:50%;background:#3a6fa8;display:inline-block}
.copyright{position:absolute;top:1172px;left:0;width:1090px;height:28px;background:var(--navy);color:#fff;font-size:11px;text-align:center;line-height:28px}
</style>
</head>
<body>
<div class="header">
  <div class="contact-tab">Cal Us : 08 7412 5530<span class="sep">|</span>Email : service@velquor.example</div>
  <div class="brand"><div class="brand-mark"></div><span class="brand-name">VELQUOR</span></div>
  <nav class="nav"><span>Home</span><span>Cloud Solutions</span><span>Emergency Services</span><span>Testimonials</span><span>Our Clients</span><span>About Us</span></nav>
</div>
<div class="topline"></div>

<div class="hero" role="img" aria-label="Photo of a hand touching colourful tiles on a tablet screen">
  <div class="hero-title">Welcome to Our Site !</div>
  <div class="hero-sub">Work is what you do, not where you go ...</div>
  <div class="hero-arrows">
    <span class="prev"><svg width="12" height="18"><path d="M10 1 2 9l8 8" fill="none" stroke="#ddd" stroke-width="1.5"/></svg></span>
    <span class="next"><svg width="12" height="18"><path d="M2 1l8 8-8 8" fill="none" stroke="#fff" stroke-width="1.5"/></svg></span>
  </div>
</div>

<div class="features">
  <div class="feature" style="left:146px;width:268px"><h3>Brintara Skyhold</h3><div class="icon icon-cloud" role="img" aria-label="Blue cloud illustration"></div></div>
  <div class="feature" style="left:414px;width:265px"><h3>Brintara Tallowbench Suite</h3><div class="icon icon-suite" role="img" aria-label="Suite product mark"></div></div>
  <div class="feature" style="left:679px;width:265px;border-right:1px solid var(--line)"><h3>Safe &amp; Secure</h3><div class="icon icon-lock" role="img" aria-label="Padlock warning sign illustration"></div></div>
</div>

<section class="wrap about">
  <h2 class="section-title">What We Do ?</h2>
  <p class="first">Lorem ipsum dolor sit amet, consectetur adipisicing elit, sed do eiusmod tempor incididunt ut labore et dolore magna aliqua. Ut enim ad minim veniam, quis nostrud exercitation ullamco laboris nisi ut aliquip ex ea commodo consequat.</p>
  <p>Duis aute irure dolor in reprehenderit in voluptate velit esse cillum dolore eu fugiat nulla pariatur.</p>
  <span class="read-more">Read More...</span>
  <div class="partner-badge" role="img" aria-label="Brintara Associate badge"><div></div></div>
</section>

<div class="vline"></div>
<section class="testimonial">
  <h2 class="section-title">Client`s Testimonials</h2>
  <span class="quote-mark" style="left:0;top:32px">&ldquo;</span>
  <blockquote>You are a legend. We have an audit in progress today and I was able to illustrate a "Live" recovery. Thank you for service above and beyond the call of duty. We really appreciate that.</blockquote>
  <span class="quote-mark" style="left:205px;top:100px">&rdquo;</span>
  <div class="who">Helen Tarrow</div>
  <div class="org">Kestrel Planning</div>
  <span class="more">more...</span>
</section>

<div class="divider"></div>
<section class="wrap clients">
  <h2 class="section-title">Our Clients</h2>
  <span class="view-all">View All Our Clients</span>
  <div class="client-row">
    <div class="client">Orvane Marine</div>
    <div class="client">Holloway Ridge</div>
    <div class="client dark">Stellmark Motors</div>
    <div class="client">Tendril Care</div>
    <div class="client blue">Wellmarsh Health</div>
    <div class="client">Caldor Auto</div>
    <div class="client">Ferrin Drill</div>
  </div>
</section>

<footer class="footer">
  <div class="fcol quick" style="left:147px;top:18px">
    <a>Home</a><a>Cloud Solutions</a><a>Emergency Services</a><a>Testimonials</a><a>Our Clients</a><a>About Us</a>
  </div>
  <div class="fsep" style="left:295px"></div>
  <div class="fcol" style="left:353px"><h4>Reach Us :</h4><p style="margin-top:7px;line-height:13px">PO Box 418, Marrowdene<br>Western Australia, 6042</p></div>
  <div class="fsep" style="left:520px"></div>
  <div class="fcol" style="left:582px"><h4>Phone :</h4><div class="phone">08 7412 5530</div><h4 style="margin-top:6px">Email :</h4><div class="email">service@velquor.example</div></div>
  <div class="fsep" style="left:759px"></div>
  <div class="fcol" style="left:810px"><h4>Follow Us :</h4>
    <div class="social"><span><i></i>Gather</span><span><i></i>Murmur</span><span><i></i>Ledger</span></div>
  </div>
</footer>
<div class="copyright">Copyright © 2013 <b>Velquor</b>. All Rights Reserved.</div>
</body>
</html>
```